Book cover - Quiet Rooms, Open Doors

Book cover for Ebook (Pagelight) and wrap around print cover (Printvale) (back, front, and spine)

The book title (may slightly change by end of brief):
(MAIN TITLE) 'Quiet Rooms, Open Doors'
(SUB HEADING) 'A Week-by-Week Practical Workbook to Loosen Nervous Habits, Quieten Doubt and Build Steady Poise'
by Dr Owen Hartley

I would like a bold, stand out cover. Contemporary. I would like to avoid stereotypical images of people looking anxious or worried. I would like the design to be more uplifting and hopeful, rather than focusing on the negative aspect of anxiety, but avoiding cliched photos of people raising their hands in the air, smiling and jumping etc. The cover should appeal to both men and women.

Trim size of book cover (for PrintVale) is 5.25" x 8" back and front with a spine size of 0.477 inches

Reason: I have decided to extend the deadline by 1 more day, not because I am unhappy with the quality of the designs, but because a few designers have contacted me to explain they have had technical difficulties when submitting their files. Thanks everyone for the hard work and great designs.

Target Market(s)

Males and females (16+) who struggle with social anxiety and shyness

Industry/Entity Type

Social

Font styles to use
Serif

Requirements
Must have
• Bold cover that is modern and contemporary. For example, I like these covers:
• http://shrtlnk.example/k4Tq9Zb
• http://shrtlnk.example/m8Wv2Hn
• http://shrtlnk.example/p3Jx6Lr
• http://shrtlnk.example/t7Gd1Qe
• http://shrtlnk.example/v2Nk8Fy
• http://shrtlnk.example/w9Bh4Cs
• http://shrtlnk.example/z5Mf3Ud
Nice to have
• Open to abstract designs.
Should not have
• No stereotypical pictures of people who look anxious or worried. Avoid cliched photos of people raising their hands in the air, smiling and jumping etc.

```html
<!DOCTYPE html>
<html lang="en">
<head>
<meta charset="utf-8">
<title>Quiet Rooms, Open Doors — Front Cover</title>
<link rel="stylesheet" href="https://fonts.googleapis.com/css2?family=Arimo:wght@700&family=Mulish:wght@300;400;700&display=swap">
<style>
  :root {
    --stage-bg: #ffffff;
    --cover-pink-warm: #f39292;
    --cover-pink-cool: #f7bfd2;
    --cover-pink-mid: #f5a8b6;
    --art-rose: #ef8a92;
    --art-lilac: #c4a9c6;
    --art-snow: #f8d3df;
    --title-white: #fffafa;
    --title-red: #ea4646;
    --text-white: #ffffff;
  }
  html, body {
    margin: 0;
    padding: 0;
    width: 1200px;
    height: 1200px;
    overflow: hidden;
    background: var(--stage-bg);
  }
  .canvas {
    position: relative;
    width: 1200px;
    height: 1200px;
  }
  .cover {
    position: absolute;
    left: 232px;
    top: 50px;
    width: 736px;
    height: 1100px;
    overflow: hidden;
    background: linear-gradient(100deg, var(--cover-pink-warm) 0%, var(--cover-pink-mid) 55%, var(--cover-pink-cool) 100%);
  }
  .cover__subtitle {
    position: absolute;
    top: 80px;
    left: 0;
    width: 100%;
    margin: 0;
    text-align: center;
    font-family: "Mulish", sans-serif;
    font-weight: 400;
    font-size: 25px;
    line-height: 34px;
    color: var(--text-white);
    letter-spacing: 0.2px;
  }
  .cover__subtitle-lead {
    display: block;
    font-weight: 700;
  }
  .cover__artwork {
    position: absolute;
    left: 0;
    top: 215px;
    width: 100%;
    height: 460px;
    background: linear-gradient(180deg, var(--art-rose) 0%, var(--art-lilac) 55%, var(--art-snow) 100%);
    -webkit-mask-image: linear-gradient(180deg, transparent 0%, #000 25%, #000 70%, transparent 100%);
            mask-image: linear-gradient(180deg, transparent 0%, #000 25%, #000 70%, transparent 100%);
  }
  .cover__title {
    position: absolute;
    left: 0;
    top: 638px;
    width: 100%;
    margin: 0;
    text-align: center;
    font-family: "Arimo", sans-serif;
    font-weight: 700;
    text-transform: uppercase;
  }
  .cover__title-main {
    display: block;
    font-size: 78px;
    line-height: 100px;
    color: var(--title-white);
    letter-spacing: 1px;
  }
  .cover__title-rest {
    display: block;
    margin-top: 16px;
    font-size: 67px;
    line-height: 92px;
    color: var(--title-red);
  }
  .cover__author {
    position: absolute;
    left: 0;
    top: 992px;
    width: 100%;
    margin: 0;
    text-align: center;
    font-family: "Mulish", sans-serif;
    font-weight: 300;
    font-size: 38px;
    letter-spacing: 2px;
    color: var(--text-white);
  }
</style>
</head>
<body>
  <div class="canvas">
    <section class="cover">
      <p class="cover__subtitle">
        <span class="cover__subtitle-lead">A Week-by-Week Practical Workbook</span>
        to Loosen Nervous Habits, Quieten<br>
        Doubt and Build Steady Poise
      </p>
      <div class="cover__artwork" role="img" aria-label="Cover artwork: abstract low-poly mountain landscape in coral, rose and pale blue"></div>
      <h1 class="cover__title">
        <span class="cover__title-main">Quiet Rooms,</span>
        <span class="cover__title-rest">Open Doors</span>
      </h1>
      <p class="cover__author">by Dr Owen Hartley</p>
    </section>
  </div>
</body>
</html>
```